Flyer design for the Harvest Lantern Summit 2019 (HALSUM)

Design a flyer for our annual conference with basic information about the conference: conference logo and year, Conference name: Harvest Lantern Summit Location: Talbot Community Center (Downtown Portland)482 Wexley Street, Portland, ME 04109, Date: August 8th, 9th, 10th and 11th, 2019Start time 7:00PMI would like the following three words added to the flyer. These words describe the vision of the conference: Prophetic, Fire, Overflow,

Contact info:
Website: www.vostel.org
Phone: 207 555 3184
Email: contact@meadowcrest.org

Target Market(s)

Young adults living in the United States

Industry/Entity Type

Religious

Font styles to use
Sans Serif

Colors

Designer to choose colors to be used in the design.

Requirements
Must have
• HALSUM must logo standout, the reader should be able to take a quick look and find key info,
Should not have
• Cross image, church image

```html
<!DOCTYPE html>
<html lang="en">
<head>
<meta charset="utf-8">
<title>Harvest Lantern Summit 2019 Flyer</title>
<link rel="stylesheet" href="https://fonts.googleapis.com/css2?family=Antonio:wght@400;500;600;700&display=swap">
<style>
  :root {
    --paper: #ffffff;
    --navy: #1c2540;
    --teal: #2f5a63;
    --copper-light: #f6c08a;
    --copper-mid: #e98a2c;
    --copper-dark: #c2571b;
    --text-light: #ffffff;
  }
  * { margin: 0; padding: 0; box-sizing: border-box; }
  html, body {
    width: 849px; height: 1200px; overflow: hidden;
    background: var(--paper);
    font-family: "Antonio", "Arial Narrow", sans-serif;
  }
  .flyer {
    position: relative; width: 849px; height: 1200px; overflow: hidden;
    background: var(--paper);
  }
  .backdrop {
    position: absolute; left: 21px; top: 23px; width: 808px; height: 1153px;
    background:
      radial-gradient(circle at 52% 46%, rgba(120,50,80,0.55) 0%, rgba(60,40,70,0.25) 30%, transparent 55%),
      radial-gradient(ellipse at 0% 45%, rgba(230,200,90,0.85) 0%, rgba(200,120,60,0.55) 25%, transparent 55%),
      linear-gradient(160deg, #c98848 0%, #7c6a58 20%, var(--teal) 45%, #2d3a55 70%, var(--navy) 100%);
  }
  .headline-tags, .presenter, .date-line, .venue, .address, .tagline, .contact p {
    position: absolute; color: var(--text-light); line-height: 1; white-space: nowrap;
  }
  .headline-tags {
    top: 30px; left: 0; width: 849px; text-align: center;
    font-size: 46px; font-weight: 600; letter-spacing: 0.5px;
  }
  .presenter {
    top: 282px; left: 0; width: 849px; text-align: center;
    font-size: 64px; font-weight: 600;
    background: linear-gradient(180deg, var(--copper-light) 0%, var(--copper-mid) 50%, var(--copper-dark) 100%);
    -webkit-background-clip: text; background-clip: text; color: transparent;
  }
  .event-title { position: absolute; left: 0; top: 355px; width: 849px; height: 250px; }
  .date-line { left: 0; width: 849px; text-align: center; font-size: 70px; font-weight: 600; }
  .date-line.dates { top: 752px; }
  .date-line.start { top: 824px; }
  .divider {
    position: absolute; left: 181px; top: 911px; width: 487px; height: 2px;
    background: linear-gradient(90deg, #ffffff 0%, var(--copper-light) 40%, var(--copper-mid) 75%, var(--copper-dark) 100%);
  }
  .venue, .address { left: 0; width: 849px; text-align: center; font-size: 30px; font-weight: 500; }
  .venue { top: 937px; }
  .address { top: 977px; }
  .tagline { left: 54px; font-size: 34px; font-weight: 600; }
  .tagline.first { top: 1068px; }
  .tagline.second { top: 1105px; }
  .contact p { right: 49px; font-size: 30px; font-weight: 600; }
  .contact .web { top: 1065px; }
  .contact .phone { top: 1099px; }
  .contact .mail { top: 1133px; }
</style>
</head>
<body>
<main class="flyer">
  <div class="backdrop" role="img" aria-label="Abstract background of glowing warm light streaks and sparks over a deep navy and teal field"></div>

  <p class="headline-tags">PROPHETIC &#8226; FIRE &#8226; OVERFLOW</p>
  <p class="presenter">Vostel Presents</p>

  <svg class="event-title" viewBox="0 0 849 250" aria-label="HALSUM 2019">
    <text x="425" y="160" text-anchor="middle" textLength="700" lengthAdjust="spacingAndGlyphs"
          font-family="Antonio, sans-serif" font-weight="700" font-size="170" fill="#ffffff">HALSUM</text>
    <text x="425" y="240" text-anchor="middle" letter-spacing="30"
          font-family="Antonio, sans-serif" font-weight="700" font-size="64" fill="#ffffff">2019</text>
  </svg>

  <p class="date-line dates">AUGUST 8TH&nbsp; - 11TH 2019</p>
  <p class="date-line start">START TIME 7:00PM</p>
  <div class="divider"></div>

  <p class="venue">Talbot Community Center (Downtown Portland)</p>
  <p class="address">482 Wexley Street, Portland, ME 04109</p>

  <p class="tagline first">HARVEST LANTERN</p>
  <p class="tagline second">SUMMIT</p>

  <div class="contact">
    <p class="web">WWW.VOSTEL.ORG</p>
    <p class="phone">PH: 207 555 3184</p>
    <p class="mail">CONTACT@MEADOWCREST.ORG</p>
  </div>
</main>
</body>
</html>
```